Business Card Design Project

I am community manager and social media strategist. I need a double sided business card with company logo and name. Looking for something professional, elegant but also a little bit original.

• - The logo and the colours are the company colours and a required to stay.
- The size should be: 84 x 55 mm (or 3.30 x 2.16)
- The file size should be: 1039 x 697 pixels (300 dpi)
- I'd like rounded corners. :)

Use the following contact information for the card:

Léonie Vardin
Stratégie médias sociaux / community management / édition de sites sociaux
mob. : 0687529103
leonie.vardin@postelune.fr
Twitter. : @lvardin
Skype : vardin.leonie

```html
<!DOCTYPE html>
<html lang="fr">
<head>
<meta charset="utf-8">
<title>Léonie Vardin – Business Card</title>
<link rel="stylesheet" href="https://fonts.googleapis.com/css2?family=Open+Sans:wght@300;400&family=PT+Sans:wght@400;700&display=swap">
<style>
  :root {
    --stage-top: #f4f4f4;
    --stage-bottom: #b9b9b9;
    --label: #5a5a5a;
    --card-blue: #1d5a80;
    --card-blue-deep: #123f5f;
    --card-blue-light: #2b6d94;
    --paper-light: #f3f3f1;
    --paper-mid: #dcdcd8;
    --brand-blue: #1f5f8a;
    --ink-blue: #1a5885;
    --white: #ffffff;
  }
  * { box-sizing: border-box; margin: 0; padding: 0; }
  html, body { width: 1200px; height: 547px; overflow: hidden; }
  body {
    position: relative;
    background: linear-gradient(180deg, var(--stage-top) 0%, var(--stage-bottom) 100%);
    font-family: "PT Sans", Arial, sans-serif;
  }
  .side-label {
    position: absolute;
    top: 64px;
    width: 300px;
    text-align: center;
    font-family: "Open Sans", Arial, sans-serif;
    font-weight: 300;
    font-size: 44px;
    line-height: 1;
    color: var(--label);
  }
  .side-label--front { left: 190px; }
  .side-label--back { left: 706px; }

  .card {
    position: absolute;
    top: 140px;
    width: 506px;
    height: 322px;
    border-radius: 33px;
    overflow: hidden;
  }
  .card--front { left: 87px; }
  .card--back { left: 603px; }

  .card__texture { position: absolute; inset: 0; }
  .card--front .card__texture {
    background: radial-gradient(ellipse at 40% 30%, var(--card-blue-light) 0%, var(--card-blue) 45%, var(--card-blue-deep) 100%);
  }
  .card--back .card__texture {
    background: radial-gradient(ellipse at 50% 45%, var(--paper-light) 0%, var(--paper-mid) 100%);
  }

  .services {
    position: absolute;
    top: 26px; left: 0; right: 0;
    text-align: center;
    font-size: 13px;
    color: var(--white);
  }
  .watermark-circle {
    position: absolute;
    left: 185px; top: 55px;
    width: 70px; height: 70px;
    border-radius: 50%;
    background: rgba(255,255,255,0.12);
  }
  .watermark-name {
    position: absolute;
    left: 0; right: 0; top: 230px;
    text-align: center;
    font-size: 62px;
    font-weight: 700;
    letter-spacing: 3px;
    color: rgba(255,255,255,0.18);
  }
  .holder-name {
    position: absolute;
    top: 86px; left: 0; right: 0;
    text-align: center;
    font-size: 21px;
    font-weight: 700;
    color: var(--white);
  }
  .contact-box {
    position: absolute;
    left: 60px; top: 118px;
    width: 383px; height: 117px;
    border-radius: 18px;
    background: var(--white);
    text-align: center;
    color: var(--ink-blue);
    padding-top: 11px;
  }
  .contact-box__role {
    font-size: 16px;
    font-weight: 700;
    margin-bottom: 5px;
  }
  .contact-box__line {
    font-size: 14px;
    line-height: 17px;
  }
  .contact-box__line strong { font-weight: 700; }

  .brand-mark {
    position: absolute;
    left: 184px; top: 15px;
    width: 140px; height: 140px;
    border-radius: 50%;
    background: var(--brand-blue);
  }
  .brand-name {
    position: absolute;
    left: 0; right: 0; top: 206px;
    text-align: center;
    font-size: 57px;
    font-weight: 700;
    letter-spacing: 3px;
    color: var(--brand-blue);
  }
</style>
</head>
<body>
  <div class="side-label side-label--front">Front</div>
  <div class="side-label side-label--back">Back</div>

  <section class="card card--front">
    <div class="card__texture" role="img" aria-label="Deep blue crumpled paper texture"></div>
    <div class="watermark-circle"></div>
    <div class="watermark-name">VENTELIS</div>
    <p class="services">Stratégie médias sociaux | Community management | Édition de sites sociaux</p>
    <h1 class="holder-name">Léonie Vardin</h1>
    <div class="contact-box">
      <p class="contact-box__role">community manager and social media strategist</p>
      <p class="contact-box__line">Mob: <strong>0687529103</strong></p>
      <p class="contact-box__line">E-mail: <strong>leonie.vardin@postelune.fr</strong></p>
      <p class="contact-box__line">Twitter: <strong>@lvardin</strong></p>
      <p class="contact-box__line">Skype: <strong>vardin.leonie</strong></p>
    </div>
  </section>

  <section class="card card--back">
    <div class="card__texture" role="img" aria-label="Light grey crumpled paper texture"></div>
    <div class="brand-mark"></div>
    <div class="brand-name">VENTELIS</div>
  </section>
</body>
</html>
```